Business Cards for 41Vale

I need business cards that goes with the logo
Updates

Dear designers - many thanks for the responsesreceived to date. There are many good designs but most of them are landscape.Could you please submit a few options for portrait layout as well.

Industry/Entity Type

Business

```html
<!DOCTYPE html>
<html lang="en">
<head>
<meta charset="utf-8">
<title>41Vale Business Cards</title>
<link rel="stylesheet" href="https://fonts.googleapis.com/css2?family=Open+Sans:wght@400;600;700&display=swap">
<style>
  :root {
    --page: #ffffff;
    --ink: #3a3d40;
    --text: #2b2b2b;
    --outline: #1f1f1f;
    --red: #e2001a;
    --red-deep: #d40019;
    --red-soft: #f08394;
    --white: #ffffff;
  }
  * { margin: 0; padding: 0; box-sizing: border-box; }
  html, body {
    width: 1200px;
    height: 1061px;
    overflow: hidden;
    background: var(--page);
    font-family: "Open Sans", Arial, sans-serif;
  }
  .sheet { position: relative; width: 1200px; height: 1061px; }

  .card { position: absolute; }
  .card svg.card-shape { position: absolute; left: 0; top: 0; }

  .card-front { left: 247px; top: 80px; width: 700px; height: 400px; }
  .front-wordmark {
    position: absolute;
    left: 0; right: 0; top: 148px;
    text-align: center;
    font-weight: 700;
    font-size: 86px;
    line-height: 1;
    letter-spacing: -1px;
    color: var(--ink);
  }

  .card-back { left: 241px; top: 543px; width: 702px; height: 400px; }
  .badge {
    position: absolute;
    left: 38px; top: 130px;
    width: 156px; height: 156px;
    border-radius: 50%;
    background: var(--white);
    display: flex; align-items: center; justify-content: center;
    font-weight: 700;
    font-size: 36px;
    letter-spacing: -0.5px;
    color: var(--ink);
  }
  .website {
    position: absolute;
    left: 56px; top: 356px;
    font-size: 14px;
    color: var(--white);
  }
  .back-wordmark {
    position: absolute;
    right: 58px; top: 40px;
    font-weight: 700;
    font-size: 68px;
    line-height: 1;
    letter-spacing: -1px;
    color: var(--ink);
  }
  .contact {
    position: absolute;
    right: 58px; top: 148px;
    text-align: right;
    color: var(--text);
  }
  .contact .person { font-size: 19px; margin-bottom: 14px; }
  .contact address, .contact .lines {
    font-style: normal;
    font-size: 15px;
    line-height: 20.5px;
  }
  .contact .lines { margin-top: 20px; }
</style>
</head>
<body>
<main class="sheet">

  <section class="card card-front" aria-label="Business card front">
    <svg class="card-shape" width="700" height="400" viewBox="0 0 700 400">
      <path d="M0.75,73 A72.25,72.25 0 0 1 73,0.75 H699.25 V300 A99.25,99.25 0 0 1 600,399.25 H0.75 Z"
            fill="var(--white)" stroke="var(--outline)" stroke-width="1.5"/>
    </svg>
    <div class="front-wordmark">41Vale</div>
  </section>

  <section class="card card-back" aria-label="Business card back">
    <svg class="card-shape" width="702" height="400" viewBox="0 0 702 400">
      <defs>
        <clipPath id="back-outline">
          <path d="M0,55 A55,55 0 0 1 55,0 H702 V320 A80,80 0 0 1 622,400 H0 Z"/>
        </clipPath>
        <linearGradient id="band-fill" x1="0" y1="0" x2="1" y2="0">
          <stop offset="0" stop-color="var(--red-soft)"/>
          <stop offset="0.45" stop-color="var(--red)"/>
          <stop offset="0.75" stop-color="var(--red-deep)"/>
          <stop offset="1" stop-color="var(--red)"/>
        </linearGradient>
      </defs>
      <path d="M0,55 A55,55 0 0 1 55,0 H702 V320 A80,80 0 0 1 622,400 H0 Z" fill="var(--white)"/>
      <g clip-path="url(#back-outline)">
        <path class="side-band" d="M0,0 H225 C232,170 258,310 300,400 H0 Z" fill="url(#band-fill)"/>
      </g>
      <path d="M0.75,55 A54.25,54.25 0 0 1 55,0.75 H701.25 V320 A79.25,79.25 0 0 1 622,399.25 H0.75 Z"
            fill="none" stroke="var(--outline)" stroke-width="1.5"/>
    </svg>

    <div class="badge">41Vale</div>
    <div class="website">www.41vale.co.za</div>

    <div class="back-wordmark">41Vale</div>

    <div class="contact">
      <p class="person">Daniel Rossouw</p>
      <address>
        PO Box 71823<br>
        Meadow Ridge<br>
        0182<br>
        South Africa
      </address>
      <p class="lines">
        Tel: +27 82 555 0147<br>
        Fax: +27 86 555 0193<br>
        Email: daniel@41vale.co.za
      </p>
    </div>
  </section>

</main>
</body>
</html>
```